Building company business card

Design and print business cards for BRENTHOLM PTY LTD.
A residantial homes building company.
Mark Lantern already designed the company Logo.

```html
<!DOCTYPE html>
<html lang="en">
<head>
<meta charset="utf-8">
<title>Brentholm Pty Ltd – Business Card</title>
<link rel="stylesheet" href="https://fonts.googleapis.com/css2?family=Poppins:wght@400;600;700&display=swap">
<style>
  :root {
    --page-bg: #e9e6e4;
    --card-light: #f4f0ef;
    --gold: #c4923a;
    --navy: #0f1f6e;
    --ink: #13236b;
  }
  html, body {
    margin: 0;
    padding: 0;
    width: 1200px;
    height: 900px;
    overflow: hidden;
    background: var(--page-bg);
    font-family: "Poppins", sans-serif;
  }
  .business-card {
    position: absolute;
    left: 100px;
    top: 141px;
    width: 1000px;
    height: 618px;
    background: var(--card-light);
    overflow: hidden;
    box-shadow: 0 12px 32px rgba(0,0,0,0.18);
  }
  .card-wave {
    position: absolute;
    inset: 0;
    width: 100%;
    height: 100%;
  }
  .brand-name {
    position: absolute;
    left: 70px;
    top: 215px;
    margin: 0;
    font-size: 50px;
    font-weight: 700;
    letter-spacing: 0.5px;
    color: var(--navy);
    line-height: 1;
  }
  .holder {
    position: absolute;
    left: 60px;
    top: 420px;
    color: var(--ink);
  }
  .holder-name {
    margin: 0;
    font-size: 39px;
    font-weight: 600;
    line-height: 1.1;
    letter-spacing: 0.3px;
  }
  .holder-role {
    margin: 2px 0 0 2px;
    font-size: 28px;
    font-weight: 400;
    line-height: 1.2;
  }
  .contact-list {
    position: absolute;
    left: 592px;
    top: 307px;
    margin: 0;
    padding: 0;
    list-style: none;
    color: var(--ink);
    font-size: 28px;
    line-height: 36.5px;
  }
  .contact-list li {
    display: flex;
    align-items: center;
    gap: 10px;
  }
  .contact-icon {
    width: 26px;
    height: 26px;
    flex: none;
    fill: var(--ink);
  }
  .company-address {
    position: absolute;
    left: 592px;
    top: 472px;
    margin: 0;
    font-style: normal;
    color: var(--ink);
    font-size: 28px;
    line-height: 36.5px;
  }
  .company-address strong {
    font-weight: 700;
  }
</style>
</head>
<body>
  <article class="business-card">
    <svg class="card-wave" viewBox="0 0 1090 673" preserveAspectRatio="none" aria-hidden="true">
      <path fill="var(--navy)" d="M0,340 C150,400 320,400 520,340 S740,280 830,278 C940,278 1010,310 1090,340 L1090,673 L0,673 Z"/>
      <path fill="var(--gold)" d="M0,388 C150,425 330,405 530,352 S770,292 840,292 C950,292 1020,322 1090,348 L1090,673 L0,673 Z"/>
    </svg>

    <p class="brand-name">BRENTHOLM</p>

    <div class="holder">
      <p class="holder-name">DORIAN (DEE) KASTELL</p>
      <p class="holder-role">Director</p>
    </div>

    <ul class="contact-list">
      <li>
        <svg class="contact-icon" viewBox="0 0 24 24" aria-hidden="true"><path d="M6.6 10.8c1.4 2.8 3.8 5.1 6.6 6.6l2.2-2.2c.3-.3.7-.4 1-.2 1.1.4 2.3.6 3.6.6.6 0 1 .4 1 1V20c0 .6-.4 1-1 1C10.6 21 3 13.4 3 4c0-.6.4-1 1-1h3.5c.6 0 1 .4 1 1 0 1.3.2 2.5.6 3.6.1.3 0 .7-.2 1z"/></svg>
        <span>0412 384 590</span>
      </li>
      <li>
        <svg class="contact-icon" viewBox="0 0 24 24" aria-hidden="true"><path d="M8 1h8a2 2 0 0 1 2 2v18a2 2 0 0 1-2 2H8a2 2 0 0 1-2-2V3a2 2 0 0 1 2-2zm0 3v14h8V4zm4 15.5a1 1 0 1 0 0 2 1 1 0 0 0 0-2z"/></svg>
        <span>0467 218 443</span>
      </li>
      <li>
        <svg class="contact-icon" viewBox="0 0 24 24" aria-hidden="true"><path d="M2 5h20v14H2zm2 2v.4l8 5.2 8-5.2V7l-8 5.1z"/></svg>
        <span>dmk@brentholm-pl.com</span>
      </li>
      <li>
        <svg class="contact-icon" viewBox="0 0 24 24" aria-hidden="true"><path d="M12 2a10 10 0 1 0 0 20 10 10 0 0 0 0-20zm6.9 6h-3a15 15 0 0 0-1.3-3.9A8 8 0 0 1 18.9 8zM12 4c.8 1.2 1.5 2.5 1.9 4h-3.8c.4-1.5 1.1-2.8 1.9-4zM4.3 14a8 8 0 0 1 0-4h3.4a16 16 0 0 0 0 4zm.8 2h3a15 15 0 0 0 1.3 3.9A8 8 0 0 1 5.1 16zm3-8h-3a8 8 0 0 1 4.3-3.9A15 15 0 0 0 8.1 8zM12 20c-.8-1.2-1.5-2.5-1.9-4h3.8c-.4 1.5-1.1 2.8-1.9 4zm2.3-6H9.7a14 14 0 0 1 0-4h4.6a14 14 0 0 1 0 4zm.3 5.9a15 15 0 0 0 1.3-3.9h3a8 8 0 0 1-4.3 3.9zm1.7-5.9a16 16 0 0 0 0-4h3.4a8 8 0 0 1 0 4z"/></svg>
        <span>www.brentholm-pl.com</span>
      </li>
    </ul>

    <address class="company-address">
      <strong>BRENTHOLM PTY LTD</strong><br>
      PO Box 482<br>
      Ferndale East Vic 3197
    </address>
  </article>
</body>
</html>
```